Stationery Design for a fast food resturaunt

We just created our logo, we need nice stationary to go with it. We beed the design to be on white background and black background.

Target Market(s)

Landlords who will lease their retail shops to us. Shopping Mall Management.Real Estate Professionals.

Font styles to use
Sans Serif

```html
<!DOCTYPE html>
<html lang="en">
<head>
<meta charset="utf-8">
<title>Sunny Crate – Business Card</title>
<link href="https://fonts.googleapis.com/css2?family=Arimo:wght@400;700&display=swap" rel="stylesheet">
<style>
  :root {
    --backdrop: #e2e2e2;
    --card-dark: #1e1e1e;
    --card-light: #f3f3f3;
    --accent: #fdaa0a;
    --ink: #1f1f1f;
    --ink-soft: #333333;
    --divider: #ffffff;
    --white: #ffffff;
  }
  * { box-sizing: border-box; margin: 0; padding: 0; }
  html, body {
    width: 1200px;
    height: 900px;
    overflow: hidden;
  }
  body {
    position: relative;
    background: var(--backdrop);
    font-family: "Arimo", Arial, sans-serif;
    color: var(--ink);
  }

  .card {
    position: absolute;
    width: 466px;
    height: 265px;
  }

  /* Front: brand side */
  .card-front {
    left: 271px;
    top: 179px;
    background: var(--card-dark);
    display: flex;
    align-items: center;
    justify-content: center;
  }
  .brand-name {
    display: flex;
    align-items: center;
    gap: 14px;
    color: var(--accent);
    font-size: 38px;
    font-weight: 400;
    letter-spacing: 3px;
    margin-top: -8px;
  }
  .brand-square {
    width: 22px;
    height: 22px;
    background: var(--accent);
  }

  /* Back: contact side */
  .card-back {
    left: 490px;
    top: 414px;
    background: linear-gradient(135deg, #f7f7f7 0%, #eeeeee 100%);
    overflow: hidden;
  }
  .holder {
    position: absolute;
    left: 36px;
    top: 99px;
    width: 144px;
    text-align: center;
  }
  .holder-name {
    font-size: 17px;
    font-weight: 700;
    color: var(--ink);
    line-height: 20px;
  }
  .holder-role {
    font-size: 15px;
    color: var(--ink-soft);
    letter-spacing: 0.6px;
    line-height: 20px;
  }
  .card-divider {
    position: absolute;
    left: 204px;
    top: 56px;
    width: 1px;
    height: 130px;
    background: var(--divider);
    box-shadow: 1px 0 0 #e4e4e4;
  }
  .contact-list {
    position: absolute;
    left: 261px;
    top: 84px;
    list-style: none;
  }
  .contact-item {
    display: flex;
    align-items: center;
    gap: 6px;
    height: 25px;
    font-size: 15px;
    color: var(--ink);
  }
  .contact-icon {
    width: 18px;
    height: 18px;
    flex: none;
  }
  .accent-bar {
    position: absolute;
    left: 0;
    bottom: 0;
    width: 272px;
    height: 7px;
  }
  .web-tab {
    position: absolute;
    right: 0;
    bottom: 0;
    width: 192px;
    height: 21px;
  }
  .web-address {
    position: absolute;
    right: 0;
    bottom: 0;
    width: 182px;
    height: 21px;
    line-height: 21px;
    text-align: center;
    color: var(--white);
    font-size: 13px;
    letter-spacing: 0.8px;
  }
</style>
</head>
<body>

  <section class="card card-front" aria-label="Card front">
    <div class="brand-name">
      <span class="brand-square"></span>
      <span>SUNNY CRATE</span>
    </div>
  </section>

  <section class="card card-back" aria-label="Card back">
    <div class="holder">
      <p class="holder-name">Full Name</p>
      <p class="holder-role">Occupation</p>
    </div>

    <div class="card-divider"></div>

    <ul class="contact-list">
      <li class="contact-item">
        <svg class="contact-icon" viewBox="0 0 18 18" aria-hidden="true">
          <rect width="18" height="18" rx="3" fill="var(--accent)"/>
          <path d="M6.2 4.2 L8 6.4 L7 7.6 Q8 10 10.4 11 L11.6 10 L13.8 11.8 L12.8 13.6 Q7.8 13.4 4.4 5.2 Z" fill="var(--white)"/>
        </svg>
        <span>+01.2345.6789</span>
      </li>
      <li class="contact-item">
        <svg class="contact-icon" viewBox="0 0 18 18" aria-hidden="true">
          <rect width="18" height="18" rx="3" fill="var(--accent)"/>
          <rect x="6" y="3.5" width="6" height="11" rx="1" fill="var(--white)"/>
          <rect x="7" y="5" width="4" height="7" fill="var(--accent)"/>
        </svg>
        <span>+0123.4567</span>
      </li>
      <li class="contact-item">
        <svg class="contact-icon" viewBox="0 0 18 18" aria-hidden="true">
          <rect width="18" height="18" rx="3" fill="var(--accent)"/>
          <rect x="3.5" y="5.5" width="11" height="7.5" fill="var(--white)"/>
          <path d="M3.5 5.5 L9 10 L14.5 5.5" fill="none" stroke="var(--accent)" stroke-width="1"/>
        </svg>
        <span>contact@email.com</span>
      </li>
    </ul>

    <svg class="accent-bar" viewBox="0 0 272 7" preserveAspectRatio="none" aria-hidden="true">
      <polygon points="0,0 272,0 268,7 0,7" fill="var(--accent)"/>
    </svg>
    <svg class="web-tab" viewBox="0 0 192 21" preserveAspectRatio="none" aria-hidden="true">
      <polygon points="8,0 192,0 192,21 0,21" fill="var(--card-dark)"/>
    </svg>
    <p class="web-address">www.sunnycrate.com</p>
  </section>

</body>
</html>
```